Business Cards for Veltrin Massage and Wellness

I worked with designers from Pixel Harbor to make a wonderful logo and now I would like to use it in a business card. I have an intimate but progressive small clinical massage practice with far infrared sauna therapy for detox, vitadraw for pre and post surgery healing and ashiatsu and sports massage. We do lots of different modalities and I would like each therapist to have the same business card with their names on them. I would like to express our professionalism and connection to health.

I am attaching my logo and would like that included in the design. I love blues and greens. I would like something clean but creative, professional yet personality. I love the font copperplate gothic or I suppose whatever matches the logo. I would like to have the following information on the front of the card...

1. Logo

2. Address: Marlow Pavilion
2867 Tesslin Rd
Richmond, Va 23228
3. Phone: 804 519-2076

4. www.veltrinmassageandwellness.example

5. name of therapist, CMT (for example purposes Corin Mathers, CMT)

6. Optional information for front of card....
Far Infrared Sauna, Neuromuscular Therapy, VitaDraw, Detox Program, Deep Tissue, Swedish, Ashiatsu, Craniosacral Therapy, Reiki, Sports Massage, Couples Massage, Hot Stones, Cold Stones, LED Light Therapy

back of card...

1. Appointment Date/Time

2. Please provide 24 hours notice of cancellations

3. a line or space for appointment times.

```html
<!DOCTYPE html>
<html lang="en">
<head>
<meta charset="utf-8">
<title>Veltrin Massage and Wellness – Appointment Card</title>
<link rel="stylesheet" href="https://fonts.googleapis.com/css2?family=Cinzel:wght@400&display=swap">
<style>
  :root {
    --mint: #72cfa8;
    --olive: #9c9d4f;
    --rule: #bfe6d9;
    --paper: #ffffff;
  }
  html, body {
    margin: 0;
    padding: 0;
    width: 1200px;
    height: 734px;
    overflow: hidden;
    background: var(--paper);
  }
  .card {
    position: relative;
    width: 1200px;
    height: 734px;
    background: var(--paper);
    font-family: "Cinzel", "Times New Roman", serif;
    text-align: center;
  }
  .brand {
    position: absolute;
    top: 100px;
    left: 0;
    width: 100%;
  }
  .brand-dot {
    display: block;
    width: 74px;
    height: 74px;
    margin: 0 auto 18px;
    border-radius: 50%;
    background: var(--olive);
  }
  .brand-name {
    margin: 0;
    font-size: 22px;
    font-weight: 400;
    letter-spacing: 0.06em;
    color: var(--olive);
  }
  .appointment-heading {
    position: absolute;
    top: 286px;
    left: 0;
    width: 100%;
    margin: 0;
    font-size: 18px;
    font-weight: 400;
    letter-spacing: 0.06em;
    color: var(--mint);
  }
  .appointment-lines {
    position: absolute;
    top: 0;
    left: 0;
  }
  .cancellation-note {
    position: absolute;
    top: 480px;
    left: 0;
    width: 100%;
    margin: 0;
    font-size: 17px;
    letter-spacing: 0.06em;
    color: var(--mint);
  }
  .services {
    position: absolute;
    top: 535px;
    left: 0;
    width: 100%;
    margin: 0;
    font-size: 17px;
    line-height: 24px;
    letter-spacing: 0.03em;
    color: var(--olive);
  }
</style>
</head>
<body>
  <main class="card">
    <header class="brand">
      <span class="brand-dot" aria-hidden="true"></span>
      <p class="brand-name">Veltrin Massage and Wellness</p>
    </header>

    <h1 class="appointment-heading">YOUR APPOINTMENT DETAILS:</h1>

    <svg class="appointment-lines" width="1200" height="734" viewBox="0 0 1200 734" aria-hidden="true">
      <line x1="245" y1="354" x2="969" y2="354" stroke="var(--rule)" stroke-width="2"/>
      <line x1="245" y1="411" x2="969" y2="411" stroke="var(--rule)" stroke-width="2"/>
      <line x1="245" y1="469" x2="969" y2="469" stroke="var(--rule)" stroke-width="2"/>
    </svg>

    <p class="cancellation-note">PLEASE PROVIDE 24 HOURS NOTICE OF CANCELLATIONS.</p>

    <p class="services">
      FAR INFRARED SAUNA • NEUROMUSCULAR THERAPY • VITADRAW • DETOX PROGRAM<br>
      DEEP TISSUE SWEDISH • ASHIATSU • CRANIOSACRAL THERAPY • REIKI • SPORTS MASSAGE COUPLES<br>
      MASSAGE • HOT STONES • COLD STONES • LED LIGHT THERAPY
    </p>
  </main>
</body>
</html>
```